Letterhead Design Needed for Real Estate Office

We are a boutique real estate agency focused on property management. We need a letter head which is professional looking and include the following information:

Logo
ABN Number
Address
Postal Address
Phone
Fax
Mobile
Email
Website

Please note that the PLVAQT logo can not be changed and must be positioned at the bottom right corner.

Please find attached the existing letterhead design for all the required elements.

Target Market(s)

Letterhead mostly used for service of notices, business letters, clients communication

Industry/Entity Type

Boutique

Colors

Designer to choose colors to be used in the design.

Requirements
Must have
• Logo

```html
<!DOCTYPE html>
<html lang="en">
<head>
<meta charset="utf-8">
<title>Meridian Partners Letterhead</title>
<link href="https://fonts.googleapis.com/css2?family=Roboto+Condensed:wght@400;700&display=swap" rel="stylesheet">
<style>
  :root {
    --green-deep: #2f8a2c;
    --green-mid: #5fae2e;
    --green-light: #a9d26a;
    --grey-soft: #e3e6df;
    --grey-text: #5d5f5c;
    --ink: #1c1c1c;
    --navy: #1d3d7a;
    --paper: #ffffff;
  }
  html, body { margin: 0; padding: 0; overflow: hidden; background: var(--paper); }
  .letterhead {
    position: relative;
    width: 849px;
    height: 1200px;
    overflow: hidden;
    background: var(--paper);
    font-family: "Roboto Condensed", "Arial Narrow", sans-serif;
  }
  .brand {
    position: absolute;
    left: 28px;
    top: 34px;
    display: flex;
    align-items: center;
    gap: 14px;
  }
  .brand-mark { width: 46px; height: 46px; background: var(--green-mid); }
  .brand-name {
    font-weight: 700;
    font-size: 34px;
    line-height: 1;
    color: var(--grey-text);
    letter-spacing: 1px;
    text-transform: uppercase;
  }
  .contact {
    position: absolute;
    left: 380px;
    top: 18px;
    width: 440px;
    text-align: center;
    font-style: normal;
    font-size: 15px;
    line-height: 20px;
    color: var(--ink);
  }
  .contact p { margin: 0; }
  .header-rule {
    position: absolute;
    left: 0;
    top: 138px;
    width: 849px;
    height: 8px;
    background: var(--grey-soft);
  }
  .header-band {
    position: absolute;
    left: 0;
    top: 148px;
    width: 849px;
    height: 12px;
    background: linear-gradient(90deg, var(--green-deep), var(--green-mid) 60%, var(--green-light));
  }
  .side-accent {
    position: absolute;
    right: 0;
    top: 180px;
    width: 14px;
    height: 360px;
    background: linear-gradient(180deg, var(--grey-soft), var(--green-light));
  }
  .corner-accent {
    position: absolute;
    left: 0;
    bottom: 0;
    width: 500px;
    height: 560px;
    border-top-right-radius: 100% 100%;
    background: linear-gradient(160deg, var(--green-light), var(--green-deep));
  }
  .membership {
    position: absolute;
    right: 40px;
    bottom: 38px;
    width: 190px;
  }
  .membership-label {
    display: block;
    text-align: right;
    font-size: 17px;
    color: var(--navy);
    margin-right: 6px;
  }
  .membership-name {
    display: flex;
    align-items: center;
    gap: 10px;
  }
  .membership-mark { width: 34px; height: 34px; background: var(--navy); }
  .membership-text {
    font-weight: 700;
    font-size: 40px;
    line-height: 1;
    color: var(--navy);
  }
</style>
</head>
<body>
<main class="letterhead">
  <header>
    <div class="brand">
      <span class="brand-mark"></span>
      <span class="brand-name">Meridian<br>Partners</span>
    </div>
    <address class="contact">
      <p>ABN 42 608 214 395</p>
      <p>Shop 12B 310-326 Harbour Street Lindfield NSW 2070 AUSTRALIA</p>
      <p>PO BOX 415 Lindfield NSW 2070</p>
      <p>m 0400 555 123 | p 9000 1234</p>
      <p>f 9000 1235 | e info@mprealty.example | w http://mprealty.example</p>
    </address>
    <div class="header-rule"></div>
    <div class="header-band"></div>
  </header>

  <div class="side-accent" role="img" aria-label="Soft green accent along the right edge"></div>
  <div class="corner-accent" role="img" aria-label="Green decorative sweep in the lower left corner"></div>

  <footer class="membership">
    <span class="membership-label">member</span>
    <div class="membership-name">
      <span class="membership-mark"></span>
      <span class="membership-text">PLVAQT</span>
    </div>
  </footer>
</main>
</body>
</html>
```